Daybreak Ledger Booklet

I have a 25 page booklet that I wrote.
I need to have a book cover design, typesetting, and imagery.
I need it to be designed with bleeds because I am having it printed.
It will be in an 8.5 X 11 format.
Please look at the 2020*.png files for an idea for the cover.
The title of the mini-book is "Daybreak Ledger" .
Subtitle is "Crestlo Method for Health and Fitness Motivation"
Then in between the title and subtitle, place the "Tobin_Health_Infographic...." image.
The other images are for inside the mini-book,
The "Daybreak-Ledger-CrestlO.pdf" file is the information in the book that will need to be typesetted.
The other images are inside the book and will need to be placed inside when appropriate.
Please don't agree to do this project if you have not done this before
I also want to see your portfolio.
Thank you
P.S. I can add all my images that are in the booklet when you accept project

Target Market(s)

Baby boomers ages 50-70

Industry/Entity Type

Fitness

Colors
0a5aa6

Requirements
Must have
• My project consists of a book cover and back. And typesetting and imagery inside the book.

```html
<!DOCTYPE html>
<html lang="en">
<head>
<meta charset="utf-8">
<title>Daybreak Ledger Booklet Pages</title>
<link href="https://fonts.googleapis.com/css2?family=Lato:ital,wght@0,400;0,700;1,400;1,700&family=Roboto+Condensed:wght@700&display=swap" rel="stylesheet">
<style>
:root{
  --brand:#1a5aa8;
  --brand-dark:#0a4a94;
  --accent:#d8102a;
  --backdrop:#d2d2d2;
  --paper:#ffffff;
  --ink:#2b2b2b;
  --muted:#555;
  --shade:#e5ebf4;
}
*{margin:0;padding:0;box-sizing:border-box}
html,body{width:1200px;height:1200px;overflow:hidden;background:var(--backdrop)}
body{position:relative;font-family:'Lato',sans-serif;color:var(--ink)}
.page{position:absolute;width:410px;height:530px;background:var(--paper);box-shadow:0 2px 6px rgba(0,0,0,.25);overflow:hidden}
.page--cover{left:141px;top:28px;height:533px;background:var(--brand)}
.page--intro{left:607px;top:28px}
.page--one{left:141px;top:615px}
.page--two{left:607px;top:615px}

/* cover */
.cover-art{position:absolute;inset:0}
.cover-title{position:absolute;left:142px;top:44px;font-family:'Roboto Condensed',sans-serif;font-weight:700;color:#fff;font-size:51px;line-height:50px;letter-spacing:.3px}
.cover-subtitle{position:absolute;left:144px;top:163px;border-left:5px solid #fff;padding-left:9px;color:#fff;font-size:15px;line-height:18px;width:230px}
.cover-brand{position:absolute;left:276px;top:472px;color:#fff;font-weight:700;font-size:21px;letter-spacing:.5px}

/* intro */
.intro-band{position:absolute;left:0;top:202px;width:100%;height:99px;background:var(--brand);color:#fff;font-style:italic;font-size:8.6px;line-height:16.8px;text-align:center;padding:18px 40px 0}

/* inner pages */
.page-body{position:absolute;left:29px;top:29px;width:355px;height:470px;overflow:hidden;font-size:6.5px;line-height:10px}
.page-body p{margin-bottom:6.6px}
.section-head{display:flex;align-items:center;gap:4px;font-size:9.2px;color:var(--muted);margin:0 0 3px}
.section-head::before{content:"";width:12px;height:6px;background:var(--brand)}
.callout{color:var(--brand);font-weight:700}
.portrait{float:right;width:162px;height:170px;position:relative;margin:-14px -6px 0 6px}
.portrait-ring{position:absolute;left:21px;top:20px;width:146px;height:146px;border-radius:50%;background:var(--brand)}
.portrait-photo{position:absolute;left:8px;top:0;width:140px;height:140px;border-radius:50%;border:3px solid #fff;background:radial-gradient(circle at 45% 35%,#b4a89c,#7b6e64 60%,#4f5a7a)}
.sheet-title{position:absolute;left:28px;top:25px;width:353px;height:30px;border-top:3px double var(--brand);border-bottom:3px double var(--brand);text-align:center;font-family:'Roboto Condensed',sans-serif;font-weight:700;color:var(--brand);font-size:18px;line-height:25px}
.page--two .page-body{top:65px;height:435px}
.bullets{color:var(--brand);font-weight:700;list-style:none;margin-bottom:6px}
.bullets li::before{content:"• "}
.subhead{color:var(--brand);font-weight:700}

.page-foot{position:absolute;left:0;top:506px;width:100%;height:10px}
.page-foot svg{position:absolute;inset:0}
.foot-text{position:absolute;top:1.5px;font-size:5.6px;color:#fff}
.foot-copy{left:29px}
.foot-url{left:221px}
.foot-brand{position:absolute;left:302px;top:-1px;font-weight:700;font-size:10px;color:var(--brand)}
.foot-num{position:absolute;left:385px;top:0.5px;font-size:7px;color:#fff}
</style>
</head>
<body>

<section class="page page--cover">
  <svg class="cover-art" width="410" height="533" viewBox="0 0 410 533">
    <defs>
      <linearGradient id="beach" x1="0" y1="0" x2="0" y2="1"><stop offset="0" stop-color="#8fb6d8"/><stop offset=".55" stop-color="#6f9fc2"/><stop offset="1" stop-color="#d9c6a4"/></linearGradient>
      <linearGradient id="sky" x1="0" y1="0" x2="1" y2="1"><stop offset="0" stop-color="#c7ccd2"/><stop offset="1" stop-color="#6d747c"/></linearGradient>
      <linearGradient id="park" x1="0" y1="0" x2="0" y2="1"><stop offset="0" stop-color="#b9cfe0"/><stop offset=".5" stop-color="#8fbf5a"/><stop offset="1" stop-color="#d8d3c8"/></linearGradient>
    </defs>
    <polygon points="0,336 50,386 0,436" fill="var(--accent)"/>
    <polygon points="143,500 110,533 176,533" fill="var(--accent)"/>
    <polygon points="0,436 0,533 110,533" fill="#c9ccd2"/>
    <g role="img" aria-label="Photo of an older couple leaping joyfully on a beach">
      <rect x="-6" y="189" width="140" height="140" rx="10" transform="rotate(45 64 259)" fill="url(#beach)"/>
    </g>
    <g role="img" aria-label="Photo of a raised fist holding a medal against a cloudy sky">
      <rect x="95" y="329" width="96" height="96" rx="9" transform="rotate(45 143 377)" fill="url(#sky)"/>
    </g>
    <g role="img" aria-label="Photo of a smiling older cyclist giving a thumbs up in a park">
      <rect x="16" y="408" width="96" height="96" rx="9" transform="rotate(45 64 456)" fill="url(#park)"/>
    </g>
  </svg>
  <h1 class="cover-title">DAYBREAK<br>LEDGER</h1>
  <p class="cover-subtitle">Crestlo Method for Health and Fitness Motivation</p>
  <div class="cover-brand">Crestlo</div>
</section>

<section class="page page--intro">
  <div class="intro-band">Finally...How You Can Finally Achieve an Elite Level of Fitness...Even if You are Starting at the Age of 63...like I did! Watch Your Fitness Soar with the Newly Revealed “Crestlo Method” that Transforms you from “Exerciser” to “Athlete”</div>
</section>

<section class="page page--one">
  <div class="page-body">
    <h2 class="section-head">Forward</h2>
    <p>This ledger could change your life. I know it seems rather bold to claim that you can sit down for the next few minutes and read something that could alter the course of your life. In fact, I wouldn’t have believed it myself just a few short years ago.</p>
    <p>But three years ago, at the age of sixty-three, I started on a journey that would change my life forever. What you are reading right now is the result of three years of experimentation, reading, watching, testing, and taking ACTION that has allowed me to achieve a high degree of fitness and health in my sixties.</p>
    <p>This ledger is going to upset the “apple cart” big time. A lot of fitness trainers, local gyms, and companies in the health and fitness industry are going to be very pissed at me.</p>
    <p class="callout">But what I’ve learned is too powerful to keep to myself, so I just had to share it with you.</p>
    <p>Before we get started, spend a few moments studying the cover page of this document. It may feel a little overwhelming, but I promise you’ll understand it when you finish this ledger.</p>
    <p>As you read, my hope is that you will begin to see the “Big Takeaway.” This takeaway has changed my life. And my hope and dream is that it does the same for you.</p>
    <h2 class="section-head" style="margin-top:10px">Who is Tobin Hale</h2>
    <div class="portrait">
      <div class="portrait-ring"></div>
      <div class="portrait-photo" role="img" aria-label="Candid photo of the author relaxing on a couch at home"></div>
    </div>
    <p>First of all, I’m not the famous actor. If you did a Findora search on “Tobin Hale,” you’d get two or three pages of the Hollywood star. I’m certainly not a star and have no ambition to be one. My story isn’t made in Hollywood.</p>
    <p>Four years ago, after thirty-two years of marriage, my sixty-two-year-old wife suddenly died of a brain aneurysm while we were watching the College Football Championship game on TV. It was so fast and incredibly devastating. Unless you’ve experienced it, you don’t understand how quickly those we love can be gone.</p>
    <p>If it hadn’t been for my children and family, I would have gone into a much deeper depression than I did.</p>
    <p>Yet I did what many of us would do. I attempted to find relief in TV, food, and alcohol. As you may know, it’s very easy to put on weight when you are inactive and over sixty.</p>
    <p>To this day, I don’t recall who took this picture of me. But I’m eternally grateful for the wake-up call!</p>
    <p>I feel awkward when I start to discuss this (and I mention it only because it’s urgent that you begin to understand how powerful the methods I’m going to reveal to you are), but my transformation— starting at the age of sixty-three—is quite amazing according to friends, family, and even strangers.</p>
    <p>I’ll show you current pictures later. And I’m doing that for a reason. This ledger is about you, not me. This ledger was written for YOU! You are the hero in this story.</p>
  </div>
  <footer class="page-foot">
    <svg width="410" height="10" viewBox="0 0 410 10"><polygon points="0,0 300,0 292,10 0,10" fill="var(--brand)"/><polygon points="368,0 410,0 410,10 360,10" fill="var(--brand)"/></svg>
    <span class="foot-text foot-copy">© 2019 Northgate Resource Group LLC</span>
    <span class="foot-text foot-url">www.crestlo-method.com</span>
    <span class="foot-brand">Crestlo</span>
    <span class="foot-num">1</span>
  </footer>
</section>

<section class="page page--two">
  <h1 class="sheet-title">Purpose of Daybreak Ledger</h1>
  <div class="page-body">
    <p>To provide a proven system, for young and old alike, that gives the single-minded, competition-driven athlete a way to more energy, more muscle, less stress, better health, and victory in competition, all while committing to a simple health and fitness regimen.</p>
    <h2 class="section-head">Why Am I Sharing These Secrets with You?</h2>
    <p>I’ve already mentioned that I started this discovery a little over three years ago. There was no way I could continue on the destructive path I found myself on. I wasn’t providing anything to my family but a depressed, lazy, fat man. I initially went into this discovery with the sole purpose of helping myself. What I didn’t tell you is that everything I’ve learned and put into practice has all been for a higher purpose: I eventually realized that this needs to be shared!</p>
    <ul class="bullets">
      <li>A vision of a health and fitness system that could stand up on its own.</li>
      <li>A fitness system that didn’t need me.</li>
      <li>A fitness system that was simple and still provided you with more energy, more muscle, less stress, better health, and a competitive edge!</li>
    </ul>
    <p>I’m still working on myself. I still need to tone my mid-section a little more.</p>
    <p>But my commitment to fitness excellence will never stop. I see that as my reward and motivation: <i>constant and never-ending improvement</i>.</p>
    <h2 class="section-head" style="margin-top:10px">The Reasons Most People Fail at Fitness and Health</h2>
    <p>Take a trip to your local gym. When you arrive, look around. It’s always great to see people that are trying to improve their health, isn’t it?</p>
    <p>But nine out of ten of them are working out ALL WRONG! They are standing around. Taking too many breaks. Texting.</p>
    <p>If you take a tour of the facility, I’ll wager you’ll find somebody on a stationary bike watching a movie or playing a game on his or her phone!</p>
    <p><span class="subhead">Is somebody making them be there?</span><br>A lot of people are performing what really are (to me) ridiculous and absolutely unnecessary exercises. It almost looks like they are training just to perform tricks on a stage.</p>
    <p>And the fitness trainers . . . OUCH!</p>
    <p>It seems like they sometimes make up these funky exercises to justify their jobs. And they OVERCOMPLICATE the training so they become a crutch to the client! (Oh, boy . . . I just pissed off a bunch of fitness trainers.)</p>
    <p>And don’t get me going on all these diets for fitness. Paleo! Keto! Harbor Lite! Ardenne! They are too hard to maintain, too disruptive, and overcomplicated. Right?</p>
    <p class="callout">The <i>overwhelm</i> of fitness and health methodologies are the real reason you struggle to be and stay fit.</p>
    <p>It’s the reason you fail. You are getting so much misinformation, and the deluge of all these new fads make it impossible to fulfill your dream for a fit and active life. It’s causing you to remain unfocused and making things more complicated than they need to be. You are getting distracted and trying a whole bunch of different health and fitness tactics.</p>
  </div>
  <footer class="page-foot">
    <svg width="410" height="10" viewBox="0 0 410 10"><polygon points="0,0 300,0 292,10 0,10" fill="var(--brand)"/><polygon points="368,0 410,0 410,10 360,10" fill="var(--brand)"/></svg>
    <span class="foot-text foot-copy">© 2019 Northgate Resource Group LLC</span>
    <span class="foot-text foot-url">www.crestlo-method.com</span>
    <span class="foot-brand">Crestlo</span>
    <span class="foot-num">2</span>
  </footer>
</section>

</body>
</html>
```